New Flyer Design Project Brenwick Doors and Interiors

Real photos will be added but please start with these for layout. Copy will be supplied so you can just leave a text box to start I am open to suggestions. Thank you

Target Market(s)

Builders, Designers, remodelers, consumers

Colors

Designer to choose colors to be used in the design.

Requirements
Must have
• Before and after photos, email, phone, logo, description

```html
<!DOCTYPE html>
<html lang="en">
<head>
<meta charset="utf-8">
<title>Brenwick Doors and Interiors – Flyer</title>
<link href="https://fonts.googleapis.com/css2?family=Lato:ital,wght@0,400;0,700;0,900;1,700&display=swap" rel="stylesheet">
<style>
  :root{
    --stage:#16191d;
    --brick-light:#8e1414;
    --brick-dark:#3a0505;
    --panel:#420303;
    --band:#4a0606;
    --yellow:#e6ea1f;
    --white:#ffffff;
    --tag:#4a2c22;
    --photo-border:#f4f1ec;
  }
  *{box-sizing:border-box;margin:0;padding:0}
  html,body{width:1200px;height:848px;overflow:hidden;background:var(--stage)}
  body{display:flex;align-items:center;justify-content:center;font-family:"Lato",sans-serif}

  .flyer{
    position:relative;width:600px;height:848px;overflow:hidden;
    background:
      radial-gradient(ellipse at 85% 20%, var(--brick-light) 0%, rgba(142,20,20,0) 60%),
      linear-gradient(160deg, #5a0808 0%, #7c1010 35%, var(--brick-dark) 100%);
  }

  .brand-title{
    position:absolute;top:42px;right:36px;text-align:right;
    color:var(--yellow);font-weight:900;font-size:50px;line-height:56px;
    text-transform:uppercase;letter-spacing:.5px;
  }

  .gallery-panel{
    position:absolute;left:0;top:176px;width:600px;height:430px;background:var(--panel);
  }

  .photo{position:absolute;border:3px solid var(--photo-border);overflow:hidden}
  .photo--peeling-door{left:24px;top:190px;width:306px;height:128px;
    background:linear-gradient(120deg,#a89a8e 0%,#8f8275 40%,#6c9a80 65%,#8c6d5c 100%)}
  .photo--iron-door{left:24px;top:330px;width:306px;height:160px;border-top-right-radius:52px;
    background:linear-gradient(90deg,#6e5a45 0%,#8a735a 45%,#5d4b3a 100%)}
  .photo--white-door-top{left:344px;top:252px;width:232px;height:150px;border-top-left-radius:52px;
    background:linear-gradient(135deg,#e9e7e2 0%,#bdb8b0 55%,#8a857e 100%)}
  .photo--white-door-bottom{left:344px;top:416px;width:232px;height:178px;border-top-left-radius:52px;
    background:linear-gradient(135deg,#ecebe7 0%,#c3beb6 50%,#8d8880 100%)}

  .photo-tag{
    position:absolute;background:var(--tag);color:var(--white);
    font-weight:900;font-size:14px;letter-spacing:.5px;padding:5px 10px;text-transform:uppercase;
  }
  .photo-tag--left{left:14px;bottom:14px}
  .photo-tag--right{right:12px;bottom:12px}

  .intro-copy{
    position:absolute;left:24px;top:500px;width:306px;
    color:var(--yellow);font-weight:700;font-size:11px;line-height:14px;
  }

  .contact-band{
    position:absolute;left:0;top:606px;width:600px;height:242px;
    background:linear-gradient(180deg,var(--band) 0%,#5e0909 60%,#3d0404 100%);
    padding:26px 40px 0;
  }
  .cta{color:var(--white);font-weight:700;font-size:25px}
  .phone{color:var(--yellow);font-weight:900;font-size:66px;line-height:76px;letter-spacing:1px}
  .closing-copy{color:var(--white);font-size:13px;line-height:18px;margin-top:8px;width:440px}
</style>
</head>
<body>
  <article class="flyer">
    <h1 class="brand-title">Brenwick Doors<br>and Interiors</h1>

    <div class="gallery-panel"></div>

    <div class="photo photo--peeling-door" role="img" aria-label="Photo of a weathered door with peeling green paint">
      <span class="photo-tag photo-tag--left">After</span>
    </div>
    <div class="photo photo--iron-door" role="img" aria-label="Photo of a restored wooden door with wrought iron strap hardware">
      <span class="photo-tag photo-tag--left">After</span>
    </div>
    <div class="photo photo--white-door-top" role="img" aria-label="Photo of a worn white door with iron hinge before restoration">
      <span class="photo-tag photo-tag--right">Before</span>
    </div>
    <div class="photo photo--white-door-bottom" role="img" aria-label="Photo of a worn white door with iron hinge before restoration">
      <span class="photo-tag photo-tag--right">Before</span>
    </div>

    <p class="intro-copy">Lorem ipsum dolor sit amet, consectetur adipiscing elit. Suspendisse vestibulum feugiat elit, et posuere justo sagittis sit amet. Aliquam lacinia quam vel aliquam efficitur. Ut egestas risus a porta faucibus. Donec mauris mi, laoreet in lacus in, tincidunt pharetra massa.</p>

    <section class="contact-band">
      <p class="cta">Call Us Today For Free Estimate</p>
      <p class="phone">123 456 7890</p>
      <p class="closing-copy">Lorem ipsum dolor sit amet, consectetur adipiscing elit. Suspendisse vestibulum feugiat elit, et posuere justo sagittis sit amet. Aliquam lacinia quam vel aliquam efficitur.</p>
    </section>
  </article>
</body>
</html>
```